Redesign business cards

We have a new logo and I am not that happy with the layout of our existing card and looking for a change. Font is a bit small and the green can be hard to read. Logo may need a tidy up as the copy I have is not that hi-res too so require you to produce a hi-res version of the logo for us too. There will be three individual business cards to produce with just the names and phone numbers being different. Address will change too, but use what you see on the card for now.

Industry/Entity Type

Business

Requirements
Nice to have
• You could consider a redesign to the new logo, just not too radical. We like the blue and green hexagons as we feel that they are representative of oil industry that we are in.

```html
<!DOCTYPE html>
<html lang="en">
<head>
<meta charset="utf-8">
<title>NovaLume Oil Services – Business Cards</title>
<link rel="stylesheet" href="https://fonts.googleapis.com/css2?family=Cinzel:wght@400;600&display=swap">
<style>
  :root {
    --orange: #f8ae3f;
    --grey: #6d6e70;
    --white: #ffffff;
    --stage: #e9e6e1;
  }
  html, body {
    margin: 0;
    width: 1200px;
    height: 901px;
    overflow: hidden;
    background: var(--stage);
  }
  .card-set {
    position: relative;
    width: 1200px;
    height: 901px;
  }
  .card {
    position: absolute;
    width: 540px;
    height: 308px;
    border-radius: 28px;
    overflow: hidden;
    background: var(--orange);
    box-shadow: 0 5px 18px rgba(0,0,0,0.12);
    font-family: "Cinzel", serif;
  }
  .card--first  { left: 40px;  top: 122px; }
  .card--second { left: 620px; top: 122px; }
  .card--third  { left: 330px; top: 470px; }

  .card-art {
    position: absolute;
    inset: 0;
    width: 100%;
    height: 100%;
  }
  .brand {
    position: absolute;
    right: 32px;
    top: 70px;
    display: flex;
    align-items: center;
    gap: 12px;
  }
  .brand-mark {
    width: 28px;
    height: 28px;
    border-radius: 50%;
    background: var(--orange);
  }
  .brand-name {
    font-weight: 600;
    font-size: 22px;
    line-height: 1.15;
    color: var(--grey);
  }
  .contact {
    position: absolute;
    left: 27px;
    top: 179px;
    margin: 0;
    padding: 0;
    list-style: none;
    color: var(--white);
    font-size: 12px;
    line-height: 15.6px;
  }
  .contact li {
    display: flex;
    align-items: flex-start;
    gap: 7px;
  }
  .contact-icon {
    flex: none;
    width: 11px;
    height: 11px;
    margin-top: 2px;
  }
  .contact-indent {
    padding-left: 18px;
  }
  .person {
    position: absolute;
    right: 32px;
    bottom: 14px;
    text-align: center;
    color: var(--white);
  }
  .person-name {
    font-size: 17px;
    line-height: 21px;
    margin: 0;
    letter-spacing: 0.5px;
  }
  .person-role {
    font-size: 14px;
    line-height: 18px;
    margin: 0;
    letter-spacing: 0.5px;
  }
</style>
</head>
<body>
<div class="card-set">

  <!-- Card 1 -->
  <div class="card card--first">
    <svg class="card-art" viewBox="0 0 1000 571" preserveAspectRatio="none" aria-hidden="true">
      <path d="M-20,132 C250,332 650,462 1020,452" fill="none" stroke="#6d6e70" stroke-width="5"/>
      <path d="M-20,90 C250,290 650,420 1020,410" fill="none" stroke="#6d6e70" stroke-width="30"/>
      <path d="M-20,0 H1020 V380 C650,390 250,260 -20,40 Z" fill="#ffffff"/>
    </svg>
    <div class="brand">
      <span class="brand-mark"></span>
      <span class="brand-name">NovaLume<br>Oil Services</span>
    </div>
    <ul class="contact">
      <li><svg class="contact-icon" viewBox="0 0 16 16"><circle cx="8" cy="8" r="8" fill="#fff"/><path d="M8 3.5a3 3 0 0 0-3 3c0 2.2 3 5.5 3 5.5s3-3.3 3-5.5a3 3 0 0 0-3-3z" fill="#f8ae3f"/></svg><span>Suite # 418,</span></li>
      <li class="contact-indent"><span>Kerr Bldg, NY 10457</span></li>
      <li><svg class="contact-icon" viewBox="0 0 16 16"><circle cx="8" cy="8" r="8" fill="#fff"/><path d="M5 4l2 2-1 1.2c.6 1.2 1.6 2.2 2.8 2.8L10 9l2 2-1.3 1.3C7.5 12 4 8.5 3.7 5.3z" fill="#f8ae3f"/></svg><span>212-555-0147</span></li>
      <li><svg class="contact-icon" viewBox="0 0 16 16"><circle cx="8" cy="8" r="8" fill="#fff"/><path d="M5 4l2 2-1 1.2c.6 1.2 1.6 2.2 2.8 2.8L10 9l2 2-1.3 1.3C7.5 12 4 8.5 3.7 5.3z" fill="#f8ae3f"/></svg><span>212-555-0183</span></li>
      <li><svg class="contact-icon" viewBox="0 0 16 16"><circle cx="8" cy="8" r="8" fill="#fff"/><path d="M5 4l2 2-1 1.2c.6 1.2 1.6 2.2 2.8 2.8L10 9l2 2-1.3 1.3C7.5 12 4 8.5 3.7 5.3z" fill="#f8ae3f"/></svg><span>212-555-0129</span></li>
      <li><svg class="contact-icon" viewBox="0 0 16 16"><circle cx="8" cy="8" r="8" fill="#fff"/><rect x="4" y="5" width="8" height="6" fill="#f8ae3f"/><path d="M4 5l4 3.5L12 5" fill="none" stroke="#fff" stroke-width="1"/></svg><span>hello@novalume.example</span></li>
      <li><svg class="contact-icon" viewBox="0 0 16 16"><circle cx="8" cy="8" r="8" fill="#fff"/><circle cx="8" cy="8" r="4" fill="none" stroke="#f8ae3f" stroke-width="1.4"/><path d="M4 8h8M8 4v8" stroke="#f8ae3f" stroke-width="1"/></svg><span>www.novalume.example</span></li>
    </ul>
    <div class="person">
      <p class="person-name">Daniel Reyes</p>
      <p class="person-role">Owner / C.E.O</p>
    </div>
  </div>

  <!-- Card 2 -->
  <div class="card card--second">
    <svg class="card-art" viewBox="0 0 1000 571" preserveAspectRatio="none" aria-hidden="true">
      <path d="M-20,132 C250,332 650,462 1020,452" fill="none" stroke="#6d6e70" stroke-width="5"/>
      <path d="M-20,90 C250,290 650,420 1020,410" fill="none" stroke="#6d6e70" stroke-width="30"/>
      <path d="M-20,0 H1020 V380 C650,390 250,260 -20,40 Z" fill="#ffffff"/>
    </svg>
    <div class="brand">
      <span class="brand-mark"></span>
      <span class="brand-name">NovaLume<br>Oil Services</span>
    </div>
    <ul class="contact">
      <li><svg class="contact-icon" viewBox="0 0 16 16"><circle cx="8" cy="8" r="8" fill="#fff"/><path d="M8 3.5a3 3 0 0 0-3 3c0 2.2 3 5.5 3 5.5s3-3.3 3-5.5a3 3 0 0 0-3-3z" fill="#f8ae3f"/></svg><span>Suite # 418,</span></li>
      <li class="contact-indent"><span>Kerr Bldg, NY 10457</span></li>
      <li><svg class="contact-icon" viewBox="0 0 16 16"><circle cx="8" cy="8" r="8" fill="#fff"/><path d="M5 4l2 2-1 1.2c.6 1.2 1.6 2.2 2.8 2.8L10 9l2 2-1.3 1.3C7.5 12 4 8.5 3.7 5.3z" fill="#f8ae3f"/></svg><span>212-555-0162</span></li>
      <li><svg class="contact-icon" viewBox="0 0 16 16"><circle cx="8" cy="8" r="8" fill="#fff"/><path d="M5 4l2 2-1 1.2c.6 1.2 1.6 2.2 2.8 2.8L10 9l2 2-1.3 1.3C7.5 12 4 8.5 3.7 5.3z" fill="#f8ae3f"/></svg><span>212-555-0175</span></li>
      <li><svg class="contact-icon" viewBox="0 0 16 16"><circle cx="8" cy="8" r="8" fill="#fff"/><path d="M5 4l2 2-1 1.2c.6 1.2 1.6 2.2 2.8 2.8L10 9l2 2-1.3 1.3C7.5 12 4 8.5 3.7 5.3z" fill="#f8ae3f"/></svg><span>212-555-0129</span></li>
      <li><svg class="contact-icon" viewBox="0 0 16 16"><circle cx="8" cy="8" r="8" fill="#fff"/><rect x="4" y="5" width="8" height="6" fill="#f8ae3f"/><path d="M4 5l4 3.5L12 5" fill="none" stroke="#fff" stroke-width="1"/></svg><span>hello@novalume.example</span></li>
      <li><svg class="contact-icon" viewBox="0 0 16 16"><circle cx="8" cy="8" r="8" fill="#fff"/><circle cx="8" cy="8" r="4" fill="none" stroke="#f8ae3f" stroke-width="1.4"/><path d="M4 8h8M8 4v8" stroke="#f8ae3f" stroke-width="1"/></svg><span>www.novalume.example</span></li>
    </ul>
    <div class="person">
      <p class="person-name">Laura Brennan</p>
      <p class="person-role">Operations Manager</p>
    </div>
  </div>

  <!-- Card 3 -->
  <div class="card card--third">
    <svg class="card-art" viewBox="0 0 1000 571" preserveAspectRatio="none" aria-hidden="true">
      <path d="M-20,132 C250,332 650,462 1020,452" fill="none" stroke="#6d6e70" stroke-width="5"/>
      <path d="M-20,90 C250,290 650,420 1020,410" fill="none" stroke="#6d6e70" stroke-width="30"/>
      <path d="M-20,0 H1020 V380 C650,390 250,260 -20,40 Z" fill="#ffffff"/>
    </svg>
    <div class="brand">
      <span class="brand-mark"></span>
      <span class="brand-name">NovaLume<br>Oil Services</span>
    </div>
    <ul class="contact">
      <li><svg class="contact-icon" viewBox="0 0 16 16"><circle cx="8" cy="8" r="8" fill="#fff"/><path d="M8 3.5a3 3 0 0 0-3 3c0 2.2 3 5.5 3 5.5s3-3.3 3-5.5a3 3 0 0 0-3-3z" fill="#f8ae3f"/></svg><span>Suite # 418,</span></li>
      <li class="contact-indent"><span>Kerr Bldg, NY 10457</span></li>
      <li><svg class="contact-icon" viewBox="0 0 16 16"><circle cx="8" cy="8" r="8" fill="#fff"/><path d="M5 4l2 2-1 1.2c.6 1.2 1.6 2.2 2.8 2.8L10 9l2 2-1.3 1.3C7.5 12 4 8.5 3.7 5.3z" fill="#f8ae3f"/></svg><span>212-555-0191</span></li>
      <li><svg class="contact-icon" viewBox="0 0 16 16"><circle cx="8" cy="8" r="8" fill="#fff"/><path d="M5 4l2 2-1 1.2c.6 1.2 1.6 2.2 2.8 2.8L10 9l2 2-1.3 1.3C7.5 12 4 8.5 3.7 5.3z" fill="#f8ae3f"/></svg><span>212-555-0138</span></li>
      <li><svg class="contact-icon" viewBox="0 0 16 16"><circle cx="8" cy="8" r="8" fill="#fff"/><path d="M5 4l2 2-1 1.2c.6 1.2 1.6 2.2 2.8 2.8L10 9l2 2-1.3 1.3C7.5 12 4 8.5 3.7 5.3z" fill="#f8ae3f"/></svg><span>212-555-0129</span></li>
      <li><svg class="contact-icon" viewBox="0 0 16 16"><circle cx="8" cy="8" r="8" fill="#fff"/><rect x="4" y="5" width="8" height="6" fill="#f8ae3f"/><path d="M4 5l4 3.5L12 5" fill="none" stroke="#fff" stroke-width="1"/></svg><span>hello@novalume.example</span></li>
      <li><svg class="contact-icon" viewBox="0 0 16 16"><circle cx="8" cy="8" r="8" fill="#fff"/><circle cx="8" cy="8" r="4" fill="none" stroke="#f8ae3f" stroke-width="1.4"/><path d="M4 8h8M8 4v8" stroke="#f8ae3f" stroke-width="1"/></svg><span>www.novalume.example</span></li>
    </ul>
    <div class="person">
      <p class="person-name">Marcus Hale</p>
      <p class="person-role">Field Supervisor</p>
    </div>
  </div>

</div>
</body>
</html>
```